Tovesca Website

I need a website for a startup company that provides GIS (Geographic Information Services) staffing and products for local cities. Current website is www.tovescagroup.com

```html
<!DOCTYPE html>
<html lang="en">
<head>
<meta charset="utf-8">
<title>Tovesca Group</title>
<link href="https://fonts.googleapis.com/css2?family=Poppins:wght@300;400;500;600&display=swap" rel="stylesheet">
<style>
:root{
  --navy:#171a2b;
  --navy-deep:#121424;
  --blue:#2ba0d2;
  --blue-dark:#1c8cbc;
  --white:#ffffff;
  --ink:#1b1d2a;
  --text:#33353f;
  --card:#f3f3f3;
  --field:#f2f2f2;
}
*{margin:0;padding:0;box-sizing:border-box}
html,body{width:1200px;height:3000px;overflow:hidden}
body{background:var(--navy);font-family:"Poppins",sans-serif;color:var(--text);position:relative}
.abs{position:absolute}
.logo{font-family:"Poppins",sans-serif;font-weight:500;font-size:44px;color:var(--white);letter-spacing:-0.5px;line-height:1}
.nav{display:flex;align-items:center;gap:0;font-size:18px;color:var(--white)}
.nav a{color:inherit;text-decoration:none;position:absolute;white-space:nowrap}
.pill{display:flex;align-items:center;justify-content:center;border-radius:20px;background:var(--blue);color:var(--white);font-size:18px;font-weight:400;text-decoration:none}
.pill.outline{background:transparent;border:1.5px solid var(--white)}
.hero-art{left:466px;top:100px;width:734px;height:570px;
  background:radial-gradient(ellipse 55% 40% at 52% 48%,#1f6a5c 0%,#163e44 35%,#172434 65%,var(--navy) 100%)}
.hero-title{left:88px;top:190px;font-size:62px;font-weight:500;color:var(--white);line-height:1.2}
.hero-title .accent{color:var(--blue);font-size:76px;display:block;line-height:1.05;margin:4px 0 2px}
.sheet{left:0;top:685px;width:1200px;height:1997px;background:var(--white);border-radius:72px}
h2{font-weight:400;color:var(--ink);font-size:46px;line-height:1}
.center{text-align:center;width:1200px;left:0}
.about-text{left:150px;width:900px;top:848px;font-size:18px;line-height:31px;text-align:center;color:var(--text)}
.about-text b{font-weight:600;color:var(--ink)}
.svc-intro{left:623px;top:1057px;width:480px;font-size:18px;line-height:31px}
.card{background:var(--card);border-radius:14px;overflow:hidden}
.card h3{font-weight:400;font-size:40px;color:var(--ink);line-height:46px}
.card p{color:var(--text)}
.photo{position:absolute}
.field{position:absolute;background:var(--field);border-radius:24px;font-size:18px;color:var(--text);padding:14px 17px;height:46px}
.foot-nav a{position:absolute;color:var(--white);font-size:18px;text-decoration:none}
.social{position:absolute;width:20px;height:20px;border-radius:50%;background:var(--white)}
</style>
</head>
<body>

<header>
  <div class="abs logo" style="left:88px;top:36px">Tovesca Group</div>
  <nav class="nav">
    <a style="left:653px;top:53px">Home</a>
    <a style="left:748px;top:53px">About Us</a>
    <a style="left:863px;top:53px">Services
      <svg width="10" height="6" viewBox="0 0 10 6" style="margin-left:4px;vertical-align:middle"><path d="M1 1l4 4 4-4" fill="none" stroke="#fff" stroke-width="1.3"/></svg></a>
    <a class="pill" style="left:988px;top:48px;width:125px;height:35px">Contact Us</a>
  </nav>
</header>

<section class="hero">
  <div class="abs hero-art" role="img" aria-label="Digital terrain point cloud with a smartphone and a location pin above it"></div>
  <h1 class="abs hero-title">WE MAKE<span class="accent">GIS WORK</span>FOR YOU</h1>
  <a class="abs pill" style="left:85px;top:467px;width:126px;height:35px">Contact Us</a>
  <a class="abs pill outline" style="left:229px;top:467px;width:168px;height:36px">Services Details</a>
</section>

<main class="abs sheet"></main>

<section class="about">
  <h2 class="abs center" style="top:773px">About Us</h2>
  <p class="abs about-text">We are an innovative team of geospatial experts with <b>25 years of experience in the field of GIS.</b> We specialize in providing results-driven GIS solutions for local government and the private sector.</p>
  <a class="abs pill" style="left:534px;top:941px;width:125px;height:35px">Read More</a>
</section>

<section class="services">
  <h2 class="abs" style="left:88px;top:1058px">Our Services</h2>
  <p class="abs svc-intro">Lorem ipsum dolor sit amet consectetur adipiscing elit sed do eiusmod tempor incididunt ut labore et dolore magna aliqua.</p>

  <article class="abs card" style="left:87px;top:1213px;width:1028px;height:371px">
    <h3 class="abs" style="left:47px;top:braces;top:30px">GIS<br>Consulting</h3>
    <p class="abs" style="left:47px;top:148px;width:300px;font-size:18px;line-height:31px">Lorem ipsum dolor sit am et consectetur adipiscing elit sed do eiusmod tempor incididunt ut labore et dolore magna aliqua.</p>
    <a class="abs pill" style="left:47px;top:298px;width:136px;height:35px">Learn More</a>
    <div class="photo" role="img" aria-label="Hand holding a phone showing a city parcel map over topographic contour lines" style="left:403px;top:0;width:625px;height:371px;background:linear-gradient(120deg,#f1f2f6 0%,#c9cde0 45%,#e8c36a 62%,#3b4f93 100%)"></div>
  </article>

  <article class="abs card" style="left:87px;top:1608px;width:499px;height:477px">
    <div class="photo" role="img" aria-label="Phone showing nearby places over a city skyline with location labels" style="left:0;top:0;width:499px;height:238px;background:linear-gradient(135deg,#8fb0d0 0%,#4e6f93 50%,#233a57 100%)"></div>
    <h3 class="abs" style="left:47px;top:264px">GIS Applications</h3>
    <p class="abs" style="left:47px;top:325px;width:420px;font-size:14px;line-height:22px">Lorem ipsum dolor sit am et consectetur adipiscing elit sed do eiusmod tempor incididunt ut labore et dolore magna aliqua.</p>
    <a class="abs pill" style="left:47px;top:402px;width:136px;height:35px">Learn More</a>
  </article>

  <article class="abs card" style="left:613px;top:1608px;width:499px;height:477px">
    <div class="photo" role="img" aria-label="Glowing world map with a digital data connector and binary digits" style="left:0;top:0;width:499px;height:238px;background:linear-gradient(120deg,#1a1f6b 0%,#3a3bc2 45%,#b54fd0 70%,#2b62c9 100%)"></div>
    <h3 class="abs" style="left:45px;top:264px">Spatial Data Solutions</h3>
    <p class="abs" style="left:45px;top:325px;width:420px;font-size:14px;line-height:22px">Lorem ipsum dolor sit am et consectetur adipiscing elit sed do eiusmod tempor incididunt ut labore et dolore magna aliqua.</p>
    <a class="abs pill" style="left:45px;top:401px;width:136px;height:35px">Learn More</a>
  </article>
</section>

<section class="contact-form">
  <h2 class="abs center" style="top:2174px;font-size:51px">Interested In Learning</h2>
  <div class="field" style="left:94px;top:2278px;width:243px">First Name*</div>
  <div class="field" style="left:352px;top:2278px;width:242px">Last Name*</div>
  <div class="field" style="left:608px;top:2278px;width:242px">Email*</div>
  <div class="field" style="left:867px;top:2278px;width:241px">Phone no.*</div>
  <div class="field" style="left:94px;top:2349px;width:1014px;height:187px;border-radius:28px">Message*</div>
  <a class="abs pill" style="left:527px;top:2556px;width:148px;height:35px;background:var(--blue-dark)">Send</a>
</section>

<footer>
  <div class="abs logo" style="left:88px;top:2752px">Tovesca Group</div>
  <p class="abs" style="left:90px;top:2823px;width:380px;font-size:14px;line-height:24px;color:var(--white)">We are an innovative team of geospatial experts with 25 years of experience in the field of GIS. We specialize in providing results-driven GIS solutions for local government and the private sector.</p>
  <nav class="foot-nav">
    <a style="left:697px;top:2763px">Home</a>
    <a style="left:791px;top:2763px">About Us</a>
    <a style="left:907px;top:2763px">Services</a>
    <a style="left:1017px;top:2763px">Contact Us</a>
  </nav>
  <svg class="abs" style="left:697px;top:2826px" width="14" height="20" viewBox="0 0 14 20"><path d="M7 0C3.1 0 0 3.1 0 7c0 5 7 13 7 13s7-8 7-13c0-3.9-3.1-7-7-7zm0 9.5A2.5 2.5 0 1 1 7 4.5a2.5 2.5 0 0 1 0 5z" fill="#fff"/></svg>
  <p class="abs" style="left:730px;top:2825px;font-size:18px;color:var(--white)">418 N. Larkmoor Ave. #204 Brenwick, CA 90000</p>
  <span class="social" aria-label="Social link" style="left:947px;top:2887px"></span>
  <span class="social" aria-label="Social link" style="left:991px;top:2887px"></span>
  <span class="social" aria-label="Social link" style="left:1039px;top:2887px"></span>
  <span class="social" aria-label="Social link" style="left:1088px;top:2887px"></span>
  <div class="abs" style="left:90px;top:2940px;width:1023px;height:1px;background:rgba(255,255,255,0.6)"></div>
  <p class="abs" style="left:90px;top:2957px;font-size:14px;color:var(--white)">© Tovesca Group. All Rights Reserved.</p>
</footer>

</body>
</html>
```